Lantern Motion for Neighbors Business Cards

I need business cards for staff in a new startup. Our company name is Movrela - we train Tai Chi teachers. But our biggest project is called Lantern Motion for Neighbors - a federal project to put together free Tai Chi classes for Vets all across America. It's a young company, with a spirit of excitement, passion, a desire to do good for others (our Vets) and a modern style and sensibility. In other words, not old-fashioned Asian martial arts theme, but something new.

Industry/Entity Type

Health And Wellness

Contact Information for Business Card

The topic is ancient healing, but the company is the Pembrooks - so I'd like a card design that captures that.

Font styles to use
Sans Serif

Colors

Designer to choose colors to be used in the design.

Requirements
Nice to have
• I've got two logos - one for the company and one for the project. I want to see if we can incorporate them both without it becoming too busy.
Should not have
• Overly old-fashioned yin-yang themes.

```html
<!DOCTYPE html>
<html lang="en">
<head>
<meta charset="utf-8">
<title>Lantern Motion for Neighbors Business Cards</title>
<link href="https://fonts.googleapis.com/css2?family=Lato:wght@400;700;900&display=swap" rel="stylesheet">
<style>
  :root {
    --backdrop: #e8e3da;
    --card-white: #ffffff;
    --ink-dark: #141210;
    --brand-red: #e8323f;
    --text-grey: #3b3b3b;
    --divider: #3d6a3d;
    --tan: #e7c595;
  }
  * { margin: 0; padding: 0; box-sizing: border-box; }
  html, body {
    width: 1200px; height: 1023px; overflow: hidden;
    background: var(--backdrop);
    font-family: 'Lato', sans-serif;
  }
  .canvas { position: relative; width: 1200px; height: 1023px; }
  .card {
    position: absolute; left: 248px; width: 681px; height: 390px;
    overflow: hidden;
    box-shadow: -6px 6px 10px rgba(0,0,0,0.35);
  }
  .card-front { top: 87px; background: var(--card-white); }
  .card-back { top: 541px; background: var(--ink-dark); }

  .front-wave { position: absolute; left: 0; top: 0; width: 681px; height: 390px; }

  .company-mark {
    position: absolute; left: 92px; top: 168px;
    display: flex; align-items: center; gap: 12px;
  }
  .company-mark .dot {
    width: 26px; height: 26px; border-radius: 50%; background: var(--brand-red);
  }
  .company-mark .name {
    font-weight: 900; font-size: 40px; color: var(--brand-red); letter-spacing: 0.5px;
  }

  .divider {
    position: absolute; left: 344px; top: 66px; width: 1.5px; height: 223px;
    background: var(--divider);
  }
  .contact { position: absolute; left: 377px; top: 58px; color: var(--text-grey); }
  .contact .person {
    font-weight: 900; font-size: 36px; color: var(--brand-red); line-height: 1; letter-spacing: 0.3px;
  }
  .contact .role { font-size: 18px; margin-top: 6px; }
  .contact .address { font-size: 18px; line-height: 24px; margin-top: 16px; }
  .contact .lines { list-style: none; margin-top: 14px; }
  .contact .lines li {
    display: flex; align-items: center; gap: 15px;
    font-size: 18px; height: 34px;
  }
  .contact .lines svg { width: 18px; height: 18px; flex: none; }

  .project-mark {
    position: absolute; left: 0; top: 0; width: 681px; height: 390px;
    display: flex; align-items: center; justify-content: center; gap: 26px;
  }
  .project-mark .ring {
    width: 110px; height: 110px; border-radius: 50%;
    border: 3px solid var(--tan);
  }
  .project-mark .name {
    color: var(--tan); font-weight: 700; font-size: 34px; line-height: 1.12;
    letter-spacing: 1px; text-transform: uppercase;
  }
</style>
</head>
<body>
<main class="canvas">
  <section class="card card-front">
    <svg class="front-wave" viewBox="0 0 681 390" aria-hidden="true">
      <path d="M0 324 Q330 372 681 318 L681 390 L0 390 Z" fill="var(--ink-dark)"/>
      <path d="M230 348 Q480 356 681 326 L681 336 Q470 364 230 350 Z" fill="var(--brand-red)"/>
      <path d="M300 349 Q500 350 681 322 L681 324 Q500 353 300 351 Z" fill="var(--card-white)"/>
    </svg>

    <div class="company-mark">
      <span class="dot"></span>
      <span class="name">Movrela</span>
    </div>

    <div class="divider"></div>

    <div class="contact">
      <p class="person">JOHN SMITH</p>
      <p class="role">Managing Director</p>
      <p class="address">2345 First Address Line<br>Second Address Line, 56324</p>
      <ul class="lines">
        <li>
          <svg viewBox="0 0 24 24"><path fill="var(--brand-red)" d="M6.6 10.8a15.1 15.1 0 0 0 6.6 6.6l2.2-2.2a1 1 0 0 1 1-.25 11.4 11.4 0 0 0 3.6.57 1 1 0 0 1 1 1V20a1 1 0 0 1-1 1A17 17 0 0 1 3 4a1 1 0 0 1 1-1h3.5a1 1 0 0 1 1 1c0 1.25.2 2.45.57 3.57a1 1 0 0 1-.25 1z"/></svg>
          <span>123 456 7890</span>
        </li>
        <li>
          <svg viewBox="0 0 24 24"><rect x="2" y="5" width="20" height="14" fill="var(--brand-red)"/><path d="M2 5l10 8 10-8" fill="none" stroke="#fff" stroke-width="1.6"/></svg>
          <span>lorem@yourwebsite.com</span>
        </li>
        <li>
          <svg viewBox="0 0 24 24" fill="none" stroke="var(--brand-red)" stroke-width="1.8"><circle cx="12" cy="12" r="9.5"/><ellipse cx="12" cy="12" rx="4.5" ry="9.5"/><path d="M2.5 12h19M4 7h16M4 17h16"/></svg>
          <span>www.yourwebsite.com</span>
        </li>
      </ul>
    </div>
  </section>

  <section class="card card-back">
    <div class="project-mark">
      <span class="ring"></span>
      <p class="name">Lantern Motion<br>for Neighbors</p>
    </div>
  </section>
</main>
</body>
</html>
```